Reptile Breeder Business Cards

Im looking for a nice looking double-sided business card, using my Business Name "Basking Scales" and my logo. It should let customers know they can find me on Pictogram and Clipzy which are both BaskingScales and also my website www.baskingscales-demo.com and also gecko bazaar, Im attaching the QR code for GeckoBazaar
You can also use stock photos from online of Knob-tailed Geckos to help make the design look nice. Slogan can be "Specializing In Knob-Tailed Geckos, Cave Geckos and New Caledonia Geckos" This should be a Double Sided Card

Industry/Entity Type

Reptiles

Contact Information for Business Card

Im looking for a nice looking business card, using my Business Name "Basking Scales" and my logo. It should let customers know they can find me on Pictogram and Clipzy which are both BaskingScales and also my website www.baskingscales-demo.com and also gecko bazaar, Im attaching the QR code for GeckoBazaar You can also use stock photos from online of Knob-tailed Geckos to help make the design look nice. Slogan can be "Specializing In Knob-Tailed Geckos, Cave Geckos and New Caledonia Geckos" This should be a Double Sided Card

Requirements
Nice to have
• "Specializing In Knob-Tailed Geckos, Cave Geckos and New Caledonia Geckos"

```html
<!DOCTYPE html>
<html lang="en">
<head>
<meta charset="UTF-8">
<title>Basking Scales – Business Card</title>
<link rel="stylesheet" href="https://fonts.googleapis.com/css2?family=Baloo+2:wght@700;800&display=swap">
<style>
  :root {
    --ink: #0f121a;
    --paper: #ffffff;
    --page: #ffffff;
    --brand-orange: #f39a2e;
    --text-dark: #111111;
    --card-w: 760px;
    --card-h: 436px;
  }
  * { box-sizing: border-box; margin: 0; padding: 0; }
  html, body {
    width: 930px;
    height: 1200px;
    overflow: hidden;
    background: var(--page);
  }
  .sheet {
    position: relative;
    width: 930px;
    height: 1200px;
    display: flex;
    flex-direction: column;
    align-items: center;
    justify-content: center;
    gap: 52px;
  }
  .card {
    position: relative;
    width: var(--card-w);
    height: var(--card-h);
    background: var(--ink);
    overflow: hidden;
  }
  .card--front { border: 3px solid #000; }
  .card__curve {
    position: absolute;
    inset: 0;
    width: 100%;
    height: 100%;
  }
  .brand-name {
    position: absolute;
    font-family: "Baloo 2", sans-serif;
    font-weight: 800;
    color: var(--brand-orange);
    line-height: 0.9;
  }
  .card--front .brand-name {
    left: 52px;
    top: 150px;
    font-size: 62px;
  }
  .brand-dot {
    position: absolute;
    left: 512px;
    top: 14px;
    width: 62px;
    height: 62px;
    border-radius: 50%;
    background: var(--brand-orange);
  }
  .slogan {
    position: absolute;
    left: 390px;
    top: 138px;
    width: 330px;
    text-align: center;
    font-family: "Baloo 2", sans-serif;
    font-weight: 700;
    font-size: 16px;
    color: var(--text-dark);
  }
  .contact-list {
    position: absolute;
    left: 358px;
    top: 233px;
    list-style: none;
    display: flex;
    flex-direction: column;
    gap: 13px;
  }
  .contact-item {
    display: flex;
    align-items: center;
    gap: 14px;
    font-family: "Baloo 2", sans-serif;
    font-weight: 700;
    font-size: 27px;
    color: var(--text-dark);
    line-height: 1;
  }
  .contact-icon {
    width: 38px;
    height: 38px;
    flex: none;
  }
  .card--back {
    display: flex;
    align-items: center;
    justify-content: center;
  }
  .card--back .brand-name {
    position: static;
    font-size: 78px;
  }
</style>
</head>
<body>
<main class="sheet">

  <section class="card card--front" aria-label="Business card front">
    <svg class="card__curve" viewBox="0 0 760 436" preserveAspectRatio="none" aria-hidden="true">
      <path d="M22 436 C150 232 380 74 760 72 L760 436 Z" fill="var(--paper)"/>
    </svg>

    <p class="brand-name">Basking<br>Scales</p>
    <span class="brand-dot" aria-hidden="true"></span>

    <p class="slogan">“Specializing In Knob-Tailed Geckos”</p>

    <ul class="contact-list">
      <li class="contact-item">
        <svg class="contact-icon" viewBox="0 0 38 38" aria-hidden="true"><circle cx="19" cy="19" r="18" fill="var(--ink)"/></svg>
        @BaskingScales
      </li>
      <li class="contact-item">
        <svg class="contact-icon" viewBox="0 0 38 38" aria-hidden="true"><circle cx="19" cy="19" r="18" fill="var(--ink)"/></svg>
        @BaskingScales
      </li>
      <li class="contact-item">
        <svg class="contact-icon" viewBox="0 0 38 38" aria-hidden="true">
          <circle cx="19" cy="19" r="18" fill="var(--ink)"/>
          <g fill="none" stroke="#fff" stroke-width="1.6">
            <circle cx="19" cy="19" r="10"/>
            <ellipse cx="19" cy="19" rx="4.5" ry="10"/>
            <line x1="9" y1="19" x2="29" y2="19"/>
            <path d="M11 13.5 H27 M11 24.5 H27"/>
          </g>
        </svg>
        www.baskingscales-demo.com
      </li>
    </ul>
  </section>

  <section class="card card--back" aria-label="Business card back">
    <p class="brand-name">Basking Scales</p>
  </section>

</main>
</body>
</html>
```